business card design

i would like business cards designed. My business provides trade qualified personnel to the mining industry to work on heavy mobile equipment.
please put a excavator(digger) in the background in one design and have one design without so i can compare the difference.
also add info:
my logo(attached) and "mobile equipment repair and maintenance"
name: Derek Holloway
address: 57 Tarrowby RD Brindale North WA.
mobile: 0438120957
email: derek@ironvalemx.com

```html
<!DOCTYPE html>
<html lang="en">
<head>
<meta charset="utf-8">
<title>Ironvale Maintenance Services – Business Card</title>
<link href="https://fonts.googleapis.com/css2?family=Open+Sans:wght@400;600;700;800&display=swap" rel="stylesheet">
<style>
  :root {
    --navy: #0b1f45;
    --blue: #1f7aeb;
    --white: #ffffff;
    --ink: #1a1d24;
    --backdrop: #e6e8ec;
  }
  * { box-sizing: border-box; margin: 0; padding: 0; }
  html, body { width: 1200px; height: 970px; overflow: hidden; }
  body {
    background: var(--backdrop);
    font-family: "Open Sans", Arial, sans-serif;
    display: flex;
    flex-direction: column;
    align-items: center;
    justify-content: center;
    gap: 52px;
  }
  .card {
    width: 620px;
    height: 354px;
    position: relative;
    box-shadow: 0 10px 28px rgba(0,0,0,.18);
    overflow: hidden;
  }

  /* Front */
  .card--front {
    background: var(--navy);
    display: flex;
    flex-direction: column;
    align-items: center;
    justify-content: center;
  }
  .brand { display: flex; flex-direction: column; align-items: center; }
  .brand__name {
    font-weight: 800;
    color: var(--white);
    font-size: 78px;
    letter-spacing: 3px;
    line-height: 1;
  }
  .brand__sub {
    font-weight: 600;
    color: var(--blue);
    font-size: 17px;
    letter-spacing: 1.6px;
    margin-top: 8px;
  }
  .tagline {
    position: absolute;
    bottom: 44px;
    left: 0; right: 0;
    text-align: center;
    color: var(--white);
    font-size: 14px;
    letter-spacing: 1px;
  }

  /* Back */
  .card--back { background: var(--white); }
  .card--back .brand {
    position: absolute;
    left: 40px;
    top: 138px;
    align-items: flex-start;
  }
  .card--back .brand__name { color: var(--navy); font-size: 50px; letter-spacing: 2px; }
  .card--back .brand__sub { font-size: 10.5px; letter-spacing: 1px; margin-top: 6px; }
  .divider {
    position: absolute;
    left: 346px;
    top: 92px;
    width: 2px;
    height: 128px;
    background: var(--blue);
  }
  .contact {
    position: absolute;
    left: 372px;
    top: 92px;
    color: var(--ink);
    font-size: 14.5px;
    line-height: 1.45;
  }
  .contact__name {
    color: var(--blue);
    font-weight: 700;
    font-size: 22px;
    margin-bottom: 4px;
  }
  .contact__row { display: flex; align-items: center; gap: 10px; }
  .contact__row svg { width: 16px; height: 16px; flex: none; }
  .contact__list { margin-top: 2px; }

  .footer-rule {
    position: absolute;
    left: 0; right: 0;
    bottom: 20px;
    height: 3px;
    background: var(--blue);
  }
  .footer-band {
    position: absolute;
    left: 0; right: 0;
    bottom: 0;
    height: 14px;
    background: var(--navy);
  }
</style>
</head>
<body>

  <section class="card card--front">
    <div class="brand">
      <div class="brand__name">IRONVALE</div>
      <div class="brand__sub">MAINTENANCE SERVICES PTY LTD</div>
    </div>
    <p class="tagline">MOBILE EQUIPMENT REPAIR AND MAINTENANCE</p>
  </section>

  <section class="card card--back">
    <div class="brand">
      <div class="brand__name">IRONVALE</div>
      <div class="brand__sub">MAINTENANCE SERVICES PTY LTD</div>
    </div>

    <div class="divider"></div>

    <div class="contact">
      <div class="contact__name">Derek Holloway</div>
      <div>57 Tarrowby RD</div>
      <div>Brindale North WA</div>
      <div class="contact__list">
        <div class="contact__row">
          <svg viewBox="0 0 24 24" aria-hidden="true"><path fill="#1f7aeb" d="M6.6 10.8a15.1 15.1 0 0 0 6.6 6.6l2.2-2.2a1 1 0 0 1 1-.25 11.4 11.4 0 0 0 3.6.57 1 1 0 0 1 1 1V20a1 1 0 0 1-1 1A17 17 0 0 1 3 4a1 1 0 0 1 1-1h3.5a1 1 0 0 1 1 1c0 1.25.2 2.450.57 3.57a1 1 0 0 1-.25 1z"/></svg>
          <span>0438 120 957</span>
        </div>
        <div class="contact__row">
          <svg viewBox="0 0 24 24" aria-hidden="true"><path fill="#1f7aeb" d="M3 5h18a1 1 0 0 1 1 1v12a1 1 0 0 1-1 1H3a1 1 0 0 1-1-1V6a1 1 0 0 1 1-1zm9 7.2L20 7H4z"/></svg>
          <span>derek@ironvalemx.com</span>
        </div>
      </div>
    </div>

    <div class="footer-rule"></div>
    <div class="footer-band"></div>
  </section>

</body>
</html>
```